Business Card and Word .doc header and footer required

I need a business card designed for my cybersecurity consulting company. Also required, is a header and footer to be ued for my word documents.
Attached is the Logo design, font and rgb used.

Industry/Entity Type

Cyber Security Consulting

Contact Information for Business Card

Name, Phone, email, website

Colors
0054AA
0677BA
7BADD7
CADEEF
E8F1F8

Requirements
Must have
• Sleek, modern

```html
<!DOCTYPE html>
<html lang="en">
<head>
<meta charset="utf-8">
<title>Harrow Gate Consulting – Stationery</title>
<link rel="stylesheet" href="https://fonts.googleapis.com/css2?family=Montserrat:wght@400;500;600;700&family=Open+Sans:wght@400&display=swap">
<style>
  :root {
    --bg: #e4e5e7;
    --paper: #f3f4f6;
    --navy: #1d2638;
    --ink-blue: #2f3f97;
    --accent: #0677ba;
    --accent-soft: #7badd7;
    --body-text: #6b6e74;
    --dark-text: #2a2c31;
    --shadow: 0 18px 40px rgba(0,0,0,.18), 0 2px 6px rgba(0,0,0,.10);
  }
  * { box-sizing: border-box; margin: 0; padding: 0; }
  html, body { width: 1200px; height: 1187px; overflow: hidden; }
  body { background: var(--bg); font-family: "Open Sans", Arial, sans-serif; position: relative; }

  /* brand lockup */
  .brand { display: flex; align-items: center; gap: 12px; }
  .brand-dot { width: 38px; height: 38px; border-radius: 50%; border: 4px solid var(--accent); flex: none; }
  .brand-name {
    font-family: "Montserrat", Arial, sans-serif; font-weight: 700; color: var(--navy);
    font-size: 19px; line-height: 1.05; letter-spacing: .5px; text-transform: uppercase;
  }
  .brand-name small { display: block; font-size: 10px; letter-spacing: 4px; font-weight: 700; }

  /* letterhead */
  .letterhead {
    position: absolute; left: 60px; top: 170px; width: 580px; height: 820px;
    background: var(--paper); box-shadow: var(--shadow); padding: 48px 54px 40px;
  }
  .lh-header { display: flex; justify-content: space-between; align-items: flex-end; }
  .lh-meta { text-align: right; font-family: "Montserrat", Arial, sans-serif; color: var(--ink-blue); font-size: 10.5px; line-height: 1.5; }
  .lh-meta .label { font-weight: 500; }
  .lh-meta .label-gap { margin-top: 6px; }
  .lh-meta .recipient { font-weight: 600; font-size: 12px; margin-top: 2px; }
  .lh-meta .role { font-size: 7.5px; font-weight: 600; letter-spacing: .5px; }
  .lh-rule { height: 1px; background: var(--ink-blue); margin: 26px 0 40px; }
  .greeting { font-family: "Montserrat", Arial, sans-serif; font-size: 12px; color: var(--dark-text); margin-bottom: 24px; }
  .lh-body p { font-size: 9.6px; line-height: 1.55; color: var(--body-text); margin-bottom: 20px; }
  .signoff { font-family: "Montserrat", Arial, sans-serif; font-size: 11px; color: var(--dark-text); margin-top: 28px; }
  .signature { width: 180px; height: 70px; margin: 10px 0 6px 18px;
    background: linear-gradient(90deg, rgba(47,63,151,.16), rgba(47,63,151,.05)); }
  .signer { font-family: "Montserrat", Arial, sans-serif; font-size: 8.5px; color: var(--dark-text); margin-left: 18px; }
  .lh-footer {
    position: absolute; right: 54px; bottom: 40px; display: flex; align-items: flex-end; gap: 16px;
    font-family: "Montserrat", Arial, sans-serif; font-size: 10px; color: var(--ink-blue); line-height: 1.45; letter-spacing: .6px;
  }
  .lh-footer address { font-style: normal; }
  .divider { width: 1px; height: 52px; background: var(--ink-blue); flex: none; }

  /* business cards */
  .card { position: absolute; width: 360px; height: 206px; box-shadow: var(--shadow); }
  .card-front { left: 700px; top: 240px; background: var(--navy); display: flex; align-items: center; justify-content: center; }
  .card-front .brand-name { color: #ffffff; }
  .card-front .brand-dot { border-color: var(--accent-soft); }
  .card-back { left: 760px; top: 500px; background: var(--paper); display: flex; align-items: center; padding: 0 22px 0 26px; gap: 20px; }
  .card-back .brand-dot { width: 26px; height: 26px; border-width: 3px; }
  .card-back .brand-name { font-size: 12px; }
  .card-back .brand-name small { font-size: 6.5px; letter-spacing: 2.5px; }
  .card-back .divider { height: 110px; }
  .card-details { font-family: "Montserrat", Arial, sans-serif; color: var(--ink-blue); font-size: 7.5px; line-height: 1.5; letter-spacing: .5px; }
  .card-details .person { font-size: 11px; font-weight: 700; letter-spacing: 1px; line-height: 1.2; }
  .card-details .role { font-size: 6.5px; font-weight: 600; margin-bottom: 12px; }
  .card-details address { font-style: normal; }
  .card-details .contact { margin-top: 6px; }
</style>
</head>
<body>

<article class="letterhead">
  <header class="lh-header">
    <div class="brand">
      <span class="brand-dot"></span>
      <span class="brand-name">Harrow Gate<small>Consulting</small></span>
    </div>
    <div class="lh-meta">
      <div class="label">Date :</div>
      <div>19 October 2022</div>
      <div class="label label-gap">To :</div>
      <div class="recipient">NAME SURNAME</div>
      <div class="role">MANAGING DIRECTOR</div>
    </div>
  </header>
  <div class="lh-rule"></div>

  <p class="greeting">Hello,</p>
  <section class="lh-body">
    <p>At vero eos et accusamus et iusto odio dignissimos ducimus qui blanditiis praesentium voluptatum deleniti atque corrupti quos dolores et quas molestias excepturi sint occaecati cupiditate non provident, similique sunt in culpa qui officia deserunt mollitia animi, id est laborum et dolorum fuga. Et harum quidem rerum facilis est et expedita distinctio. Nam libero tempore, cum soluta nobis est eligendi optio cumque nihil impedit quo minus id quod maxime placeat facere possimus, omnis voluptas assumenda est, omnis dolor repellendus temporibus autem.</p>
    <p>At vero eos et accusamus et iusto odio dignissimos ducimus qui blanditiis praesentium voluptatum deleniti atque corrupti quos dolores et quas molestias excepturi sint occaecati cupiditate non provident, similique sunt in culpa qui officia deserunt mollitia animi, id est laborum et dolorum fuga. Et harum quidem rerum facilis est et expedita distinctio. Nam libero tempore, cum soluta nobis est eligendi optio cumque nihil impedit quo minus id quod maxime placeat facere possimus, omnis voluptas assumenda est, omnis dolor repellendus temporibus autem.</p>
    <p>At vero eos et accusamus et iusto odio dignissimos ducimus qui blanditiis praesentium voluptatum deleniti atque corrupti quos dolores et quas molestias excepturi sint occaecati cupiditate non provident, similique sunt in culpa qui officia deserunt mollitia animi, id est laborum et dolorum fuga. Et harum quidem rerum facilis est et expedita distinctio. Nam libero tempore, nihil impedit quo minus id quod maxime placeat facere possimus, omnis voluptas assumenda est, omnis dolor repellendus temporibus autem.</p>
  </section>

  <p class="signoff">Best regards,</p>
  <div class="signature" role="img" aria-label="Handwritten signature"></div>
  <p class="signer">Elena Ruth Marsh</p>

  <footer class="lh-footer">
    <address>10 Sample Street<br>Brookfield, NY 10001<br>United States</address>
    <span class="divider"></span>
    <div>+1-555-010-2040<br>hello@hgc.example<br>www.hgc.example</div>
  </footer>
</article>

<div class="card card-front">
  <div class="brand">
    <span class="brand-dot"></span>
    <span class="brand-name">Harrow Gate<small>Consulting</small></span>
  </div>
</div>

<div class="card card-back">
  <div class="brand">
    <span class="brand-dot"></span>
    <span class="brand-name">Harrow Gate<small>Consulting</small></span>
  </div>
  <span class="divider"></span>
  <div class="card-details">
    <div class="person">NAME SURNAME</div>
    <div class="role">MANAGING DIRECTOR</div>
    <address>10 Sample Street<br>Brookfield, NY 10001<br>United States</address>
    <div class="contact">+1-555-010-2040<br>hello@hgc.example<br>www.hgc.example</div>
  </div>
</div>

</body>
</html>
```